Web Design Project - Event Management Company

A web-page design needs to be created for an event management company. The logo has already been created, the design needs to draw on the themes and colors of the logo and extend on that.

The event management company likes to differentiate itself from others by being a bit "un-conventional" and being able to think outside the box.

the specialise in corporate events, weddings, AGMs, anything that requires coordination of resources. They also can provide Audio Visual services such as recording events.

final design will also require HTML implementation

```html
<!DOCTYPE html>
<html lang="en">
<head>
<meta charset="utf-8">
<title>Odd Tile Group</title>
<link href="https://fonts.googleapis.com/css2?family=Tinos:wght@400;700&display=swap" rel="stylesheet">
<style>
:root{
  --page-bg:#ebe7e2;
  --page-bg-light:#f4f1ed;
  --panel:#ffffff;
  --nav:#58a4bb;
  --nav-active:#70c3dc;
  --heading:#2e2424;
  --subtle:#8c8181;
  --body:#8a7f7f;
  --rule:#e4dfdc;
  --brand-square:#f07c2c;
}
*{margin:0;padding:0;box-sizing:border-box}
html,body{width:1200px;height:981px;overflow:hidden}
body{
  position:relative;
  background:radial-gradient(ellipse at 50% 30%,var(--page-bg-light),var(--page-bg) 80%);
  font-family:"Tinos",Georgia,serif;
  color:var(--body);
}
.abs{position:absolute}
.brand-mark{left:241px;top:10px;width:62px;height:62px;background:var(--brand-square)}
.brand-name{left:384px;top:20px;font-size:46px;font-weight:400;color:#ffffff;letter-spacing:1px;text-transform:uppercase;line-height:1}
.hero{left:211px;top:88px;width:775px;height:351px;
  background:linear-gradient(180deg,#efe9df 0%,#d9cdb9 45%,#c7b49a 75%,#e5dccf 100%)}
.nav{left:509px;top:156px;width:433px;height:93px;background:var(--nav)}
.nav-active{left:558px;top:148px;width:62px;height:107px}
.nav-list{left:509px;top:193px;width:433px;list-style:none;display:flex;font-size:13.5px;font-weight:700;color:#fff;text-transform:uppercase}
.nav-list li{position:absolute;white-space:nowrap}
.slider-dots{left:764px;top:383px;display:flex;gap:10px}
.dot{width:28px;height:28px;border-radius:50%;background:#fff}
.dot.is-current{background:#000}
.content{left:211px;top:439px;width:775px;height:481px;background:var(--panel)}
.heading{font-size:19px;font-weight:700;color:var(--heading);line-height:1}
.subheading{font-size:16px;color:var(--subtle);line-height:20.5px}
.text{font-size:10.5px;line-height:18px;color:var(--body)}
.name{font-size:16px;color:var(--subtle);line-height:1}
.meeting-photo{left:244px;top:584px;width:156px;height:104px;
  background:linear-gradient(100deg,#5a1d24 0%,#8c2a35 45%,#b9b4ae 80%,#d8d4cf 100%)}
.col-divider{left:565px;top:493px;width:1px;height:388px;background:var(--rule)}
.scroll-track{left:954px;top:523px;width:7px;height:195px;background:#eeeae8}
.scroll-thumb{left:954px;top:523px;width:7px;height:34px;background:var(--nav)}
.h-rule{left:604px;top:744px;width:354px;height:1px;background:var(--rule)}
.footer{left:241px;top:952px;font-size:10px;font-weight:700;color:#5a4f4f;letter-spacing:.2px}
.indent{text-indent:27px}
</style>
</head>
<body>
<header>
  <div class="abs brand-mark"></div>
  <div class="abs brand-name">Odd Tile Group</div>
</header>

<div class="abs hero" role="img" aria-label="Photo of an elegant marquee banquet hall with round tables, white chair covers and candelabras"></div>

<nav>
  <div class="abs nav"></div>
  <svg class="abs nav-active" viewBox="0 0 62 107" aria-hidden="true">
    <polygon points="0,0 62,0 62,107 31,99 0,107" fill="var(--nav-active)"/>
  </svg>
  <ul class="abs nav-list">
    <li style="left:63px">Main</li>
    <li style="left:115px">About Us</li>
    <li style="left:194px">Events</li>
    <li style="left:264px">Gallery</li>
    <li style="left:338px">Contacts</li>
  </ul>
  <div class="abs slider-dots">
    <span class="dot"></span><span class="dot is-current"></span><span class="dot"></span><span class="dot"></span>
  </div>
</nav>

<main>
  <div class="abs content"></div>

  <section class="welcome">
    <h1 class="abs heading" style="left:241px;top:486px">Welcome To Odd Tile Group</h1>
    <p class="abs subheading" style="left:240px;top:519px;width:300px">We Create Unforgettable Ideas And Events For you</p>
    <div class="abs meeting-photo" role="img" aria-label="Photo of a boardroom table lined with red chairs"></div>
    <p class="abs text" style="left:410px;top:581px;width:138px">Sed ut perspiciatis unde omnis iste natus error sit voluptatem accusantium doloremque lau&shy;dantium, totam rem aperiam, eaque ipsa quae ab illo inven&shy;tore veritatis et quasi architecto</p>
    <p class="abs text" style="left:243px;top:699px;width:305px">Sed ut perspiciatis unde omnis iste natus error sit voluptatem accusan&shy;tium doloremque laudantium, totam rem aperiam, eaque ipsa quae ab</p>
    <p class="abs text indent" style="left:243px;top:758px;width:305px">Nam libero tempore, cum soluta nobis est eligendi optio cumque nihil impedit quo minus id quod maxime placeat facere possimus, omnis voluptas assumenda est, omnis dolor repellendus. Temporibus autem quibusdam et aut officiis debitis aut rerum necessitatibus saepe eveniet ut et voluptates repudiandae sint et molestiae non recusandae.</p>
  </section>

  <div class="abs col-divider"></div>

  <section class="testimonials">
    <h2 class="abs heading" style="left:605px;top:486px">Testimonials</h2>
    <h3 class="abs name" style="left:602px;top:523px">Mira Tessel</h3>
    <p class="abs text" style="left:604px;top:552px;width:330px">Nam libero tempore, cum soluta nobis est eligendi optio cumque nihil impedit quo minus id quod maxime placeat facere possimus, omnis voluptas assumenda est, omnis dolor repellendus. Temporibus autem quibusdam et aut officiis debitis aut rerum necessitatibus saepe eveniet ut et voluptates repudiandae sint et molestiae non recusandae.</p>
    <h3 class="abs name" style="left:602px;top:660px">Daniel R.</h3>
    <p class="abs text" style="left:601px;top:684px;width:335px">Temporibus autem quibusdam et aut officiis debitis aut rerum necessitatibus saepe eveniet ut et voluptates repudiandae sint et molestiae non recusandae.</p>
    <div class="abs scroll-track"></div>
    <div class="abs scroll-thumb"></div>
  </section>

  <div class="abs h-rule"></div>

  <section class="about">
    <h2 class="abs heading" style="left:605px;top:760px">A Little About Us</h2>
    <p class="abs text indent" style="left:604px;top:795px;width:330px">Nam libero tempore, cum soluta nobis est eligendi optio cumque nihil impedit quo minus id quod maxime placeat facere possimus, omnis voluptas assumenda est, omnis dolor repellendus. Temporibus autem quibusdam et aut officiis debitis aut rerum necessitatibus saepe eveniet ut et voluptates repudiandae sint et molestiae non recusandae.</p>
  </section>
</main>

<footer class="abs footer">2012&nbsp; | &nbsp;PRIVACY POLICY</footer>
</body>
</html>
```